Tarrant Physiotherapy needs a brochure that will highlight and sell our services to prospective clie

Tarrant Physiotherapy. The treatment you need , the care you deserve.

We need a brochure design for our musculoskeletal physiotherapy business. It needs to sell our service to prospective clients and to referrers and communicate our values and mission. It needs to incorporate our services of: back and neck pain, muscle and joint sprains and strains, sports injury management, including video assessment, acupuncture, Pilates, women's health/pelvic floor physio, deep tissue massage. We use technology including video analysis to improve patient outcomes. Our website is http://tarrantphysio.example.nz attached are some images from web site and some graphics including our logo

Ideally a front page with our logo and graphics and bulletin points of our services

Sports Injuries
Back , neck and joint pain
Orthopedic rehabilitation
Acupuncture
Pelvic floor Physiotherapy

Then inside our USP's why us (see our web site) plus ....
We provide expert diagnosis of your problem and committed/dedicated to providing the best possible solution to get you back to what you love and improve your performance
Also we specialise in the use of technology with video analysis (http://www.kelvaro.example.com/), digital postural analysis software (http://stancegrid.example.com/mobile/), computer graphics for education (http://apps.vornexa.example.com/joint_view) and video/online exercise programs (https://www.drelmora.example.org/index.php), online booking (http://bookings.quintaro.example.com/tarrant/)
Long appointments , not rushed , to give us time to help

Then sections for:

Physiotherapy
sports physio
Orthopaedic rehab
back and neck pain
acupuncture
women's health inside
take info from our website, but also I can upload brochures from Rehab Collective, take the best out of each of those and combine with our web info to provide description for each.

And on back all contact detail and QR code for our website

Target Market(s)

mostly 40 to 60 comfortably off, educated, active, some sporty, healthy, middle class

Industry/Entity Type

Education

Requirements
Must have
• Must match our website with the logo and pictures on home page
brochure to be A4 trifold DLE, please match our font or use one we can use easily
Nice to have
• not too busy, give our customers good reasons to use our services,

```html
<!DOCTYPE html>
<html lang="en">
<head>
<meta charset="utf-8">
<title>Tarrant Physiotherapy – Trifold Brochure</title>
<link href="https://fonts.googleapis.com/css2?family=Montserrat:wght@400;600;700&family=Open+Sans:wght@400;600&display=swap" rel="stylesheet">
<style>
  :root{
    --orange:#f08a1e;
    --orange-deep:#e0761a;
    --ink:#555b62;
    --ink-dark:#3f4449;
    --paper:#fbfbf9;
    --paper-grey:#eeeeec;
    --canvas:#dcdcdc;
    --white:#ffffff;
  }
  *{box-sizing:border-box;margin:0;padding:0}
  html,body{width:1033px;height:1200px;overflow:hidden}
  body{background:var(--canvas);font-family:"Open Sans",Arial,sans-serif;color:var(--ink);position:relative}
  .spread{position:absolute;left:106px;width:820px;height:580px;display:flex;background:var(--paper);box-shadow:0 4px 14px rgba(0,0,0,.18)}
  .spread--outside{top:13px}
  .spread--inside{top:607px}
  .panel{position:relative;width:273px;height:580px;overflow:hidden;border-right:1px solid #e2e2df}
  .panel:last-child{border-right:none}
  .panel--wide{width:547px}
  .photo{position:absolute}
  .heading{font-family:"Montserrat",Arial,sans-serif;font-weight:600}
  .logo{display:flex;align-items:center;gap:7px;font-family:"Montserrat",Arial,sans-serif;font-weight:600;color:var(--ink-dark);line-height:1.05}
  .logo-mark{width:14px;height:14px;background:var(--orange);flex:none}
  .badge-shape{background:var(--orange);border-radius:8px}

  /* outside: inner flap */
  .difference{position:absolute;left:0;top:0;width:273px;height:330px;background:var(--orange);color:var(--white);padding:22px 18px 0 30px}
  .difference h2{font-size:16px;margin-bottom:6px;position:relative}
  .difference h2::before{content:"";position:absolute;left:-30px;top:-2px;width:18px;height:22px;background:var(--paper);border-radius:0 4px 4px 0}
  .difference p{font-size:10px;line-height:1.45;margin-bottom:16px}

  /* outside: back panel */
  .back{background:var(--paper-grey);padding:22px 20px}
  .back .logo{font-size:15px}
  .book{margin-top:22px;font-family:"Montserrat",Arial,sans-serif;color:var(--orange)}
  .book-title{font-size:34px;font-weight:700;line-height:1}
  .book-sub{font-size:11px;font-weight:600;letter-spacing:.5px;color:var(--ink)}
  .book-now{font-size:9px;color:var(--orange);margin-top:2px}
  .phone-big{font-family:"Montserrat",Arial,sans-serif;font-weight:600;font-size:22px;color:var(--ink);margin-top:12px}
  .contact-band{position:absolute;left:0;top:340px;width:273px;height:68px;display:flex;align-items:center;gap:40px;padding-left:14px}
  .pin-block{width:60px;height:60px;background:var(--orange);border-radius:0 8px 8px 0;display:flex;align-items:center;justify-content:center}
  .member{font-size:8px;color:var(--ink)}
  .member .badge-shape{width:56px;height:56px;margin-top:2px}
  .address{position:absolute;left:20px;top:430px;font-family:"Montserrat",Arial,sans-serif;font-size:12px;line-height:1.4;color:var(--ink-dark)}
  .phones{position:absolute;left:20px;top:518px;font-family:"Montserrat",Arial,sans-serif;font-size:13px;color:var(--ink-dark);line-height:1.6}
  .phones div{display:flex;align-items:center;gap:8px}

  /* outside: cover */
  .tagline{position:absolute;left:0;width:100%;top:22px;text-align:center;font-family:"Montserrat",Arial,sans-serif;font-size:17px;line-height:1.45;color:var(--ink);font-weight:600}
  .tagline em{font-style:normal;color:var(--orange)}
  .cover-band{position:absolute;left:0;top:420px;width:273px;height:100px;display:flex;align-items:center;padding-left:24px}
  .cover-band::before{content:"";position:absolute;left:0;top:0;width:273px;height:16px;background:var(--orange)}
  .cover-band::after{content:"";position:absolute;left:0;top:0;width:20px;height:100px;background:var(--orange)}
  .cover-band .logo{font-size:17px;margin-left:10px}
  .website{position:absolute;left:0;top:530px;width:100%;text-align:center;font-family:"Montserrat",Arial,sans-serif;font-size:14px;color:var(--orange);border-top:1px solid var(--orange);margin:0;padding-top:8px}

  /* inside: services */
  .services{padding:18px 16px 0 30px}
  .service{margin-bottom:10px}
  .service h3{font-size:12.5px;color:var(--ink-dark);position:relative;margin-bottom:3px}
  .service h3::before{content:"";position:absolute;left:-30px;top:-1px;width:20px;height:18px;background:var(--orange);border-radius:0 4px 4px 0}
  .service p{font-size:8.6px;line-height:1.38;color:var(--orange-deep)}

  /* inside: technology + why us */
  .tech-title{position:absolute;left:24px;top:16px;font-family:"Montserrat",Arial,sans-serif;font-weight:600;font-size:13px;color:var(--orange);border-bottom:2px solid var(--orange);padding-bottom:4px;width:500px}
  .tech-row{position:absolute;left:24px;top:52px;display:flex;gap:16px}
  .tech-item{display:flex;align-items:center;gap:5px;font-size:8.5px;line-height:1.2;color:var(--ink-dark);width:110px}
  .tech-icon{width:34px;height:30px;flex:none;border-radius:3px}
  .tech-badge{position:absolute;left:24px;top:104px;font-size:8px}
  .tech-badge .badge-shape{width:58px;height:54px;margin-top:2px}
  .promise{position:absolute;z-index:2;left:285px;top:100px;width:240px;font-size:10px;line-height:1.45;color:var(--ink-dark);text-align:right}
  .promise .q{color:var(--orange);font-weight:700;font-size:14px;line-height:1}
  .treatment-photo{left:60px;top:232px;width:487px;height:248px}
  .appointments{position:absolute;left:0;top:488px;width:547px;font-family:"Montserrat",Arial,sans-serif;font-size:13px;font-weight:600;color:var(--ink);padding-left:40px;border-bottom:3px solid var(--orange);padding-bottom:3px}
  .bottom-band{position:absolute;left:0;top:512px;width:547px;height:68px;display:flex;align-items:center;justify-content:space-between;padding:0 24px 0 40px}
  .bottom-band::before{content:"";position:absolute;left:0;top:0;width:18px;height:68px;background:var(--orange)}
  .bottom-band .logo{font-size:15px}
  .bottom-book{font-family:"Montserrat",Arial,sans-serif;color:var(--orange);line-height:1}
  .bottom-book strong{font-size:24px;font-weight:700;display:block}
  .bottom-book span{font-size:9px;color:var(--ink);font-weight:600}
  .bottom-phone{font-family:"Montserrat",Arial,sans-serif;font-weight:600;font-size:21px;color:var(--ink)}
</style>
</head>
<body>

<section class="spread spread--outside" aria-label="Brochure outside">
  <div class="panel">
    <div class="difference">
      <h2 class="heading">The Tarrant Difference</h2>
      <p>We care about you and your health and are absolutely dedicated to providing you with the best possible service. Our highly trained, experienced, professional Physiotherapists are committed to giving you the best outcomes to resolve your problem.</p>
      <h2 class="heading">We Make It Easy</h2>
      <p>We are CSA Registered and no referral from a Dr is needed. We will register your injury with CSA if necessary. We work as a team referring you to your GP or to a specialist if it is required and communicating with them about your progress.</p>
    </div>
    <div class="photo" role="img" aria-label="Photo of a physiotherapist stretching an older woman's arm" style="left:0;top:330px;width:273px;height:250px;background:linear-gradient(135deg,#f3efe9 0%,#d9c3ae 45%,#9fb46a 75%,#f1ece4 100%)"></div>
  </div>

  <div class="panel back">
    <div class="logo"><span class="logo-mark"></span>Tarrant<br>Physiotherapy</div>
    <div class="book">
      <div class="book-title">Book</div>
      <div class="book-sub">AN APPOINTMENT</div>
      <div class="book-now">Book Now ▼</div>
    </div>
    <div class="phone-big">0800 418 273</div>
    <div class="photo" role="img" aria-label="Street map showing the clinic location" style="left:0;top:210px;width:273px;height:120px;background:linear-gradient(160deg,#e6e6e4,#cfcfcc)"></div>
    <div class="contact-band">
      <div class="pin-block">
        <svg width="24" height="32" viewBox="0 0 24 32" aria-hidden="true"><path d="M12 1C6 1 2 5.5 2 11c0 7.5 10 19 10 19s10-11.5 10-19C22 5.5 18 1 12 1z" fill="#fff"/><circle cx="12" cy="11" r="4" fill="#f08a1e"/></svg>
      </div>
      <div class="member">Member of<div class="badge-shape"></div></div>
    </div>
    <div class="address">Tarrant Physiotherapy<br>14 Harlow Avenue<br>Tarrant<br>Auckland 0600</div>
    <div class="phones">
      <div><svg width="12" height="12" viewBox="0 0 24 24" aria-hidden="true"><path d="M6.6 10.8a15 15 0 006.6 6.6l2.2-2.2c.3-.3.7-.4 1-.2 1.1.4 2.3.6 3.6.6.6 0 1 .4 1 1V20c0 .6-.4 1-1 1A17 17 0 013 4c0-.6.4-1 1-1h3.5c.6 0 1 .4 1 1 0 1.3.2 2.5.6 3.6.1.3 0 .7-.2 1z" fill="#f08a1e"/></svg>09 555 0142</div>
      <div><svg width="12" height="12" viewBox="0 0 24 24" aria-hidden="true"><rect x="6" y="1" width="12" height="22" rx="2" fill="#f08a1e"/><rect x="8" y="4" width="8" height="13" fill="#fff"/></svg>021 555 873</div>
    </div>
  </div>

  <div class="panel">
    <p class="tagline"><em>Treatment</em> you need<br>Care <em>you</em> deserve</p>
    <div class="photo" role="img" aria-label="Photo of a woman stretching her arms overhead at sunset" style="left:0;top:82px;width:273px;height:338px;background:linear-gradient(180deg,#ffffff 0%,#f4ece2 55%,#e9b36e 85%,#b9884e 100%)"></div>
    <div class="cover-band">
      <div class="logo"><span class="logo-mark"></span>Tarrant<br>Physiotherapy</div>
    </div>
    <p class="website">tarrantphysio.example.nz</p>
  </div>
</section>

<section class="spread spread--inside" aria-label="Brochure inside">
  <div class="panel services">
    <div class="service">
      <h3 class="heading">Physiotherapy</h3>
      <p>Physiotherapy is a health care profession primarily concerned with the remediation of impairments and disabilities. All of our therapists have over ten years of experience in managing musculo-skeletal conditions.</p>
    </div>
    <div class="service">
      <h3 class="heading">Sports Physio</h3>
      <p>The most common sporting injuries (according to CSA) are to the head, shoulders, hamstrings, knees and ankles. Most sports injuries are easily preventable, which is where a physio comes in. They can help you rehabilitate from an injury, show you how to prevent one occurring or work with you to improve your sporting performance.</p>
    </div>
    <div class="service">
      <h3 class="heading">Women Health</h3>
      <p>Pregnancy, menopause, gynecological procedures and a history of back pain or pelvic pain can all lead to either pelvic floor weakness or dysfunction. Other risk factors include being overweight, a chronic cough or sneeze along with repeat heavy lifting.</p>
    </div>
    <div class="service">
      <h3 class="heading">Acupuncture</h3>
      <p>Acupuncture is used by physiotherapists to achieve pain relief via the stimulation of the nervous system, such as the brain and spinal cord to produce the body's own pain relieving neuro-chemicals, such as endorphins for pain relief, melatonin to promote sleep and serotonin to promote well being.</p>
    </div>
    <div class="photo" role="img" aria-label="Photo of a woman in a kneeling yoga stretch" style="left:0;top:470px;width:273px;height:110px;background:linear-gradient(180deg,#ffffff 0%,#efe9e3 60%,#d7c6b6 100%)"></div>
  </div>

  <div class="panel panel--wide">
    <div class="tech-title">We specialise in the use of technology in treatment</div>
    <div class="tech-row">
      <div class="tech-item"><span class="tech-icon" role="img" aria-label="Video analysis app screen" style="background:linear-gradient(135deg,#6a6f75,#2f3236)"></span>Video<br>Analysis</div>
      <div class="tech-item"><span class="tech-icon" role="img" aria-label="Postural analysis tablet screen" style="background:linear-gradient(135deg,#7fa6c9,#2f3236)"></span>Digital<br>Postural<br>Analysis</div>
      <div class="tech-item"><span class="tech-icon" role="img" aria-label="Anatomy graphics screen" style="background:linear-gradient(135deg,#c98a5c,#3b3b3b)"></span>Computer<br>Graphics for<br>Education</div>
      <div class="tech-item"><span class="tech-icon" role="img" aria-label="Exercise program screen" style="background:linear-gradient(135deg,#9fc3e6,#3a7fbf)"></span>Online<br>Exercise<br>Programs</div>
    </div>
    <div class="tech-badge">Member of<div class="badge-shape"></div></div>
    <p class="promise"><span class="q">“</span> We guarantee that we will provide a professional service to your satisfaction. We pride ourselves on the delivery of the highest quality physiotherapy, massage, acupuncture and rehabilitation services. Our philosophy is that if YOU are not happy then WE are not happy. <span class="q">”</span></p>
    <div class="photo treatment-photo" role="img" aria-label="Photo of a physiotherapist treating a patient's leg on a treatment table" style="background:linear-gradient(180deg,#ffffff 0%,#eeeae5 45%,#d8cbbd 75%,#f2eee9 100%)"></div>
    <div class="appointments">Long appointments, not rushed, lot of time for us to help</div>
    <div class="bottom-band">
      <div class="logo"><span class="logo-mark"></span>Tarrant<br>Physiotherapy</div>
      <div class="bottom-book"><strong>Book</strong><span>AN APPOINTMENT</span></div>
      <div class="bottom-phone">0800 418 273</div>
    </div>
  </div>
</section>

</body>
</html>
```